High End Craft Beer needs a label design update

We would like to update the design of our line of craft beer, named Maurice-Edmond. The brand name needs to stay predominant in the design. We initially launched with 2 flavours, but with the addition of the third product, we feel there is not enough differentiation between each flavour, and customers are confused in which flavour they are buying (BELGIAN WHITE, INDIA PALE ALE, and AMBER ALE are the current flavours).

We plan to launch a BLONDE LAGER product, but need the 4 products to be more differentiated between each other.

We are looking for the design of the 3 current products (and also the BLOND LAGER if possible) that would be more differentiated.
Updates

Reason: Hello, I am still looking for options, so I am extending the dead-line by 5 days. Thanks

Target Market(s)

Males (75%), 21 to 40.

Font styles to use
Serif
Sans Serif

Requirements
Must have
• All 4 labels need to be coherent between themselves, but more differentiated than the current design
Should not have
• We don't want to completely "re-brand" the product, as customers currently really like the products and its design. And current customers need to easily "recognize" the product they like at store level. The only problem is the confusion between the flavours.

```html
<!DOCTYPE html>
<html lang="fr">
<head>
<meta charset="utf-8">
<title>Maurice Edmond – étiquettes</title>
<link rel="stylesheet" href="https://fonts.googleapis.com/css2?family=Josefin+Sans:wght@400;600;700&family=Open+Sans:wght@400;600&display=swap">
<style>
  :root {
    --page: #ffffff;
    --ink: #1e1e1e;
    --outline: #dcdcdc;
    --ipa-main: #0f5a3e;
    --ipa-tint: #a9c4b7;
    --amber-main: #b5651d;
    --amber-tint: #f0cfae;
    --white-main: #8c8c8c;
    --white-tint: #dcdcdc;
    --scene-dark: #1c0e08;
    --scene-warm: #7a4322;
  }
  * { box-sizing: border-box; margin: 0; padding: 0; }
  html, body { width: 1200px; height: 975px; overflow: hidden; background: var(--page); }
  .board { position: relative; width: 1200px; height: 975px; }

  .label { position: absolute; top: 80px; width: 320px; height: 415px; color: var(--ink); }
  .label--ipa   { left: 88px;  --main: var(--ipa-main);   --tint: var(--ipa-tint); }
  .label--amber { left: 448px; --main: var(--amber-main); --tint: var(--amber-tint); }
  .label--white { left: 808px; --main: var(--white-main); --tint: var(--white-tint); }
  .label__shape { position: absolute; inset: 0; }
  .label__shape .edge  { fill: #fff; stroke: var(--outline); stroke-width: 1; }
  .label__shape .frame { fill: none; stroke: var(--main); stroke-width: 9; }
  .label__shape .inner { fill: none; stroke: var(--tint); stroke-width: 4; }
  .label__shape .brewery { font-family: "Josefin Sans", sans-serif; font-weight: 700; font-size: 10.5px; letter-spacing: 1.4px; fill: var(--ink); }

  .label__portrait {
    position: absolute; left: 112px; top: 86px; width: 96px; height: 100px;
    border-radius: 48px 48px 6px 6px;
    background: linear-gradient(180deg, var(--tint) 0%, color-mix(in srgb, var(--tint) 55%, #fff) 100%);
    opacity: .75;
  }
  .label__brand {
    position: absolute; left: 0; right: 0; top: 190px; text-align: center;
    font-family: "Josefin Sans", sans-serif; font-weight: 700; font-size: 42px; line-height: 38px;
    letter-spacing: 1px; color: var(--tint); text-shadow: 3px 3px 0 var(--ink);
  }
  .label__flavour {
    position: absolute; left: 0; right: 0; top: 272px; text-align: center;
    font-family: "Josefin Sans", sans-serif; font-weight: 700; font-size: 21px; letter-spacing: 1px;
    color: var(--tint); text-shadow: 1.5px 1.5px 0 var(--main);
  }
  .label--white .label__flavour { text-shadow: 1.5px 1.5px 0 var(--white-main); }
  .label__origin {
    position: absolute; left: 0; right: 0; top: 302px; text-align: center;
    font-family: "Open Sans", sans-serif; font-size: 12.5px; letter-spacing: 1px; color: var(--ink);
  }
  .label__note {
    position: absolute; top: 330px; font-family: "Open Sans", sans-serif; font-size: 7.5px; line-height: 9px;
    color: var(--ink);
  }
  .label__note--left { left: 46px; }
  .label__note--right { right: 46px; text-align: right; }
  .label__volume {
    position: absolute; left: 0; right: 0; top: 348px; text-align: center;
    font-family: "Josefin Sans", sans-serif; font-weight: 700; font-size: 23px; color: var(--ink);
  }
  .label__volume small { font-size: 13px; }

  .scenes { position: absolute; left: 81px; top: 548px; width: 1047px; height: 320px; display: flex; }
  .scene { height: 100%; }
  .scene--ipa   { width: 364px; background: linear-gradient(125deg, var(--scene-dark) 0%, #5c3118 35%, #c9b89a 55%, #6b3a1f 75%, var(--scene-dark) 100%); }
  .scene--amber { width: 307px; background: radial-gradient(ellipse 60% 70% at 60% 60%, #c07a35 0%, var(--scene-warm) 40%, var(--scene-dark) 85%); }
  .scene--white { width: 153px; background: radial-gradient(ellipse 35% 65% at 50% 58%, #a0642f 0%, #4a2412 55%, var(--scene-dark) 90%); }
  .scene--close { width: 223px; background: linear-gradient(90deg, #3a1d0e 0%, #8c6a48 18%, #d9ccb4 50%, #8c6a48 82%, #3a1d0e 100%); }
</style>
</head>
<body>
<main class="board">

  <article class="label label--ipa">
    <svg class="label__shape" viewBox="0 0 320 415" aria-hidden="true">
      <defs><path id="arc-ipa" d="M 40 82 Q 160 26 280 82"/></defs>
      <path class="edge" d="M 26 16 Q 160 -10 294 16 L 294 40 Q 294 58 314 58 L 314 352 Q 294 352 294 372 L 294 392 Q 160 428 26 392 L 26 372 Q 26 352 6 352 L 6 58 Q 26 58 26 40 Z"/>
      <path class="frame" d="M 36 26 Q 160 2 284 26 L 284 48 Q 284 68 304 68 L 304 342 Q 284 342 284 362 L 284 384 Q 160 416 36 384 L 36 362 Q 36 342 16 342 L 16 68 Q 36 68 36 48 Z"/>
      <path class="inner" d="M 48 38 Q 160 16 272 38 L 272 58 Q 272 78 292 78 L 292 332 Q 272 332 272 352 L 272 374 Q 160 402 48 374 L 48 352 Q 48 332 28 332 L 28 78 Q 48 78 48 58 Z"/>
      <text class="brewery"><textPath href="#arc-ipa" startOffset="50%" text-anchor="middle">* BRASSERIE DEUX PINS *</textPath></text>
    </svg>
    <div class="label__portrait" role="img" aria-label="Portrait gravé du fondateur"></div>
    <h2 class="label__brand">MAURICE<br>EDMOND</h2>
    <p class="label__flavour">INDIA PALE ALE</p>
    <p class="label__origin">BRASSÉE AU QUÉBEC</p>
    <p class="label__note label__note--left">BIÈRE FORTE<br>STRONG BEER</p>
    <p class="label__note label__note--right">6,2%<br>ALC.&nbsp;VOL.</p>
    <p class="label__volume">500<small>ML</small></p>
  </article>

  <article class="label label--amber">
    <svg class="label__shape" viewBox="0 0 320 415" aria-hidden="true">
      <defs><path id="arc-amber" d="M 40 82 Q 160 26 280 82"/></defs>
      <path class="edge" d="M 26 16 Q 160 -10 294 16 L 294 40 Q 294 58 314 58 L 314 352 Q 294 352 294 372 L 294 392 Q 160 428 26 392 L 26 372 Q 26 352 6 352 L 6 58 Q 26 58 26 40 Z"/>
      <path class="frame" d="M 36 26 Q 160 2 284 26 L 284 48 Q 284 68 304 68 L 304 342 Q 284 342 284 362 L 284 384 Q 160 416 36 384 L 36 362 Q 36 342 16 342 L 16 68 Q 36 68 36 48 Z"/>
      <path class="inner" d="M 48 38 Q 160 16 272 38 L 272 58 Q 272 78 292 78 L 292 332 Q 272 332 272 352 L 272 374 Q 160 402 48 374 L 48 352 Q 48 332 28 332 L 28 78 Q 48 78 48 58 Z"/>
      <text class="brewery"><textPath href="#arc-amber" startOffset="50%" text-anchor="middle">* BRASSERIE DEUX PINS *</textPath></text>
    </svg>
    <div class="label__portrait" role="img" aria-label="Portrait gravé du fondateur"></div>
    <h2 class="label__brand">MAURICE<br>EDMOND</h2>
    <p class="label__flavour">AMBER ALE AMBRÉE</p>
    <p class="label__origin">BRASSÉE AU QUÉBEC</p>
    <p class="label__note label__note--left">BIÈRE FORTE<br>STRONG BEER</p>
    <p class="label__note label__note--right">6,2%<br>ALC.&nbsp;VOL.</p>
    <p class="label__volume">500<small>ML</small></p>
  </article>

  <article class="label label--white">
    <svg class="label__shape" viewBox="0 0 320 415" aria-hidden="true">
      <defs><path id="arc-white" d="M 40 82 Q 160 26 280 82"/></defs>
      <path class="edge" d="M 26 16 Q 160 -10 294 16 L 294 40 Q 294 58 314 58 L 314 352 Q 294 352 294 372 L 294 392 Q 160 428 26 392 L 26 372 Q 26 352 6 352 L 6 58 Q 26 58 26 40 Z"/>
      <path class="frame" d="M 36 26 Q 160 2 284 26 L 284 48 Q 284 68 304 68 L 304 342 Q 284 342 284 362 L 284 384 Q 160 416 36 384 L 36 362 Q 36 342 16 342 L 16 68 Q 36 68 36 48 Z"/>
      <path class="inner" d="M 48 38 Q 160 16 272 38 L 272 58 Q 272 78 292 78 L 292 332 Q 272 332 272 352 L 272 374 Q 160 402 48 374 L 48 352 Q 48 332 28 332 L 28 78 Q 48 78 48 58 Z"/>
      <text class="brewery"><textPath href="#arc-white" startOffset="50%" text-anchor="middle">* BRASSERIE DEUX PINS *</textPath></text>
    </svg>
    <div class="label__portrait" role="img" aria-label="Portrait gravé du fondateur"></div>
    <h2 class="label__brand">MAURICE<br>EDMOND</h2>
    <p class="label__flavour">BLANCHE WHITE</p>
    <p class="label__origin">BRASSÉE AU QUÉBEC</p>
    <p class="label__note label__note--left">BIÈRE FORTE<br>STRONG BEER</p>
    <p class="label__note label__note--right">6,2%<br>ALC.&nbsp;VOL.</p>
    <p class="label__volume">500<small>ML</small></p>
  </article>

  <section class="scenes">
    <div class="scene scene--ipa" role="img" aria-label="Photo rapprochée d'une bouteille India Pale Ale étiquetée, inclinée, avec gouttes de condensation"></div>
    <div class="scene scene--amber" role="img" aria-label="Photo d'un tonneau en bois, d'une bouteille Amber Ale et d'un verre de bière mousseuse"></div>
    <div class="scene scene--white" role="img" aria-label="Photo d'une bouteille Blanche White sur fond sombre"></div>
    <div class="scene scene--close" role="img" aria-label="Photo rapprochée de l'étiquette Blanche White couverte de condensation"></div>
  </section>

</main>
</body>
</html>
```